Website for a start-up named Vlm Quarvex.

The company is currently producing a sustainable tactical training measure for soldiers in the defense industry. We’d like a simple website design. As the product hasn’t been launched yet, we will not tell too much about the product and it’s not for sale either. We have a website on wix called vlmquarvex.com which we would like to proceed with. The design just needs a professional and loving touch. We develop an add on for TK40 rifles.

Target Market(s)

Defense industry

Industry/Entity Type

Defense

Coding

Coded - Design and coding required

Number of Pages Required

1 page

```html
<!DOCTYPE html>
<html lang="en">
<head>
<meta charset="utf-8">
<title>Vlm Quarvex</title>
<link rel="stylesheet" href="https://fonts.googleapis.com/css2?family=Roboto:ital,wght@0,400;0,500;0,700;1,700&family=Rubik:wght@400;500&display=swap">
<style>
:root{
  --teal:#0aa89a;
  --teal-dark:#078a7f;
  --blue:#3b5fa6;
  --ink:#222831;
  --text:#4a4a4a;
  --muted:#8a8a8a;
  --panel:#f4f4f4;
  --white:#ffffff;
  --line:#bfe3df;
}
*{box-sizing:border-box;margin:0;padding:0}
html,body{width:1200px;height:3125px;overflow:hidden}
body{position:relative;background:var(--white);font-family:"Roboto",sans-serif;color:var(--text)}
.abs{position:absolute}
.heading{font-family:"Rubik",sans-serif;font-weight:400;color:var(--ink);letter-spacing:.8px}
.rule{position:absolute;height:2px;background:var(--teal)}
.body-text{font-size:11.5px;line-height:15px;color:var(--text)}
.btn{position:absolute;display:flex;align-items:center;justify-content:center;font-family:"Rubik",sans-serif;font-size:14px;border-radius:2px}
.btn-solid{background:var(--teal);color:var(--white)}
.btn-outline-dark{border:1.5px solid var(--ink);color:var(--ink)}
.btn-outline-teal{border:1.5px solid var(--teal);color:var(--teal);text-transform:uppercase;letter-spacing:.4px}

/* nav */
.site-nav{position:absolute;left:0;top:0;width:1200px;height:62px;background:var(--white)}
.brand{position:absolute;left:87px;top:20px;font-family:"Rubik",sans-serif;font-weight:500;font-size:20px;color:var(--teal)}
.nav-links{position:absolute;left:258px;top:24px;display:flex;gap:19px;font-size:11.5px;color:var(--ink)}
.nav-links .active{color:var(--teal);border-bottom:2px solid var(--teal);padding-bottom:6px}
.nav-cta{left:991px;top:10px;width:121px;height:43px;font-size:14px}

/* hero */
.hero{position:absolute;left:0;top:62px;width:1200px;height:511px;background:linear-gradient(100deg,#0aab9b 0%,#1492a1 50%,#3b5fa6 100%)}
.hero-eyebrow{position:absolute;left:278px;top:125px;font-size:13px;color:#173a48;text-transform:uppercase}
.hero-title{position:absolute;left:278px;top:143px;font-family:"Rubik",sans-serif;font-size:31px;color:var(--white)}
.hero-copy{position:absolute;left:300px;top:188px;width:600px;text-align:center;font-size:11.5px;line-height:15px;color:var(--white)}
.hero .btn-solid{left:458px;top:291px;width:130px;height:43px}
.hero .btn-outline-dark{left:607px;top:291px;width:135px;height:43px;border-color:#18364a;color:#18364a}

/* who */
.who{position:absolute;left:0;top:636px;width:1200px;height:456px;background:var(--panel)}
.who-photo{position:absolute;left:691px;top:0;width:509px;height:456px;background:linear-gradient(90deg,#c9c9c9,#7a7a7a 45%,#5a5a5a 60%,#cfcfcf)}

.tech-title{position:absolute;left:0;top:1155px;width:1200px;text-align:center;font-size:22px;text-transform:uppercase;letter-spacing:1.2px}

/* tech */
.tech{position:absolute;left:0;top:1214px;width:1200px;height:736px;background:var(--panel)}
.illus-checklist{position:absolute;left:87px;top:66px;width:493px;height:266px;background:linear-gradient(135deg,#eaeaea,#f7f7f7)}
.illus-road{position:absolute;left:681px;top:406px;width:431px;height:300px;background:linear-gradient(160deg,#f4f4f4 30%,#cfcfcf 60%,#0aa89a 100%)}

/* quote */
.quote-band{position:absolute;left:0;top:2013px;width:1200px;height:228px;background:linear-gradient(100deg,#0aab9b,#1886a0);color:var(--white);text-align:center}
.quote{position:absolute;left:0;top:59px;width:1200px;font-style:italic;font-weight:700;font-size:13.5px}
.quote-author{position:absolute;left:0;top:89px;width:1200px;font-weight:500;font-size:11.5px}
.quote-band .btn{left:530px;top:147px;width:140px;height:43px;background:var(--white);color:var(--teal);text-transform:uppercase}

/* contact */
.contact{position:absolute;left:0;top:2304px;width:1200px;height:581px;background:var(--panel)}
.label{position:absolute;font-size:11px;color:var(--muted)}
.field{position:absolute;background:var(--white);border-radius:2px;font-size:11px;color:var(--ink);padding:16px 10px 0}
.contact .btn-solid{left:87px;top:487px;width:145px;height:43px;text-transform:uppercase}
.map{position:absolute;left:604px;top:0;width:596px;height:455px;background:radial-gradient(circle at 50% 50%,#4a4a4a,#303030)}
.info{position:absolute;top:482px;font-size:11px}
.info-label{color:var(--ink);display:flex;align-items:center;gap:5px}
.info-value{color:var(--muted);margin-top:6px}
.divider{position:absolute;top:471px;width:1px;height:110px;background:var(--line)}

/* footer */
.site-footer{position:absolute;left:0;top:2946px;width:1200px;height:179px;background:var(--panel)}
.footer-brand{position:absolute;left:55px;top:62px;font-family:"Rubik",sans-serif;font-weight:500;font-size:36px;color:var(--teal)}
.footer-links{position:absolute;left:414px;top:76px;display:flex;gap:18px;font-size:11.5px;color:var(--ink)}
.social{position:absolute;left:997px;top:71px;display:flex;gap:14px}
.social span{width:21px;height:21px;border-radius:50%;background:var(--ink)}
.copyright{position:absolute;left:0;top:148px;width:1200px;text-align:center;font-size:11px;color:var(--text)}
</style>
</head>
<body>

<header class="site-nav">
  <div class="brand">Vlm Quarvex</div>
  <nav class="nav-links">
    <span class="active">Home</span><span>Company</span><span>Book Online</span><span>About Us</span><span>FAQs</span><span>Contact US</span>
  </nav>
  <div class="btn btn-solid nav-cta">Contact Us</div>
</header>

<section class="hero">
  <div class="hero-eyebrow">Welcome in Vlm Quarvex.</div>
  <h1 class="hero-title">Sustainable Solutions To The Defense Industry</h1>
  <p class="hero-copy">Welcome To Vlm Quarvex, The Advanced Technology Company Paving The Way To The Future. We Are A Team Of Like-Minded And Determined Individuals, All Sharing A Vision For Success. We Believe That Our Sophisticated Technology Has The Potential To Become An Industry Sensation. Would You Like To Find Out More? Our Website Will Be Updated On A Regular Basis</p>
  <div class="btn btn-solid">Get In Touch</div>
  <div class="btn btn-outline-dark">Explore More</div>
</section>

<section class="who">
  <h2 class="heading abs" style="left:87px;top:98px;font-size:22px">Who we are</h2>
  <div class="rule" style="left:87px;top:128px;width:182px"></div>
  <p class="body-text abs" style="left:87px;top:164px;width:428px">Vlm Quarvex Is A Leading Provider Of Cutting-Edge Technologies And Services, Offering Scalable Solutions For The Defense And Security Industry Of All Sizes. Founded By A Group Of Friends Who Started By Scribbling Their Ideas On A Bus Ride In San Francisco. Today We Are Working On Innovative Solutions To Disrupt The Training Industry With A Sustainable Solution.</p>
  <div class="btn btn-outline-dark" style="left:87px;top:270px;width:135px;height:43px">Explore More</div>
  <div class="who-photo" role="img" aria-label="Photograph of a bronze war memorial statue of soldiers"></div>
</section>

<h2 class="heading tech-title">Our Innovative Technology</h2>

<section class="tech">
  <div class="illus-checklist" role="img" aria-label="Illustration of a woman walking beside a checklist with ticked items"></div>
  <h2 class="heading abs" style="left:691px;top:70px;font-size:22px">The Possibilities Are Endless</h2>
  <div class="rule" style="left:691px;top:100px;width:345px"></div>
  <p class="body-text abs" style="left:691px;top:135px;width:422px">At Vlm Quarvex, Our Comprehensive Technological Solutions Help The Industry To Become More Sustainable And Efficient With The Spendings. We Will Balance Qualitative Training Experience For Soldiers And Security Forces With Real Life Experiences And A Real Life Feel.</p>

  <h2 class="heading abs" style="left:87px;top:404px;font-size:22px">Our environment matter</h2>
  <div class="rule" style="left:87px;top:434px;width:335px"></div>
  <p class="body-text abs" style="left:87px;top:470px;width:425px">Our Platform Will Have A Wide Range Of Features Created With The Aim To Help The Industry Become More Aware Of Their Environmental Footprint. In Order To Empower Our Users To Do Better, Vlm Quarvex Is Continually Building Upon Its Technology, So Stay In Touch To Learn About Upgrades And Other Changes. For A Free Demo, Feel Free To Contact Us.</p>
  <div class="btn btn-outline-teal" style="left:87px;top:581px;width:135px;height:43px">Contact Us</div>
  <div class="illus-road" role="img" aria-label="Illustration of a person standing on a hill beside a winding road and bare trees"></div>
</section>

<section class="quote-band">
  <p class="quote">"The Secret Of Getting Ahead Is Getting Started"</p>
  <p class="quote-author">Elias Varn</p>
  <div class="btn">Get Started</div>
</section>

<section class="contact">
  <h2 class="heading abs" style="left:87px;top:42px;font-size:22px">Get In touch</h2>
  <div class="rule" style="left:87px;top:72px;width:182px"></div>
  <p class="body-text abs" style="left:87px;top:90px;width:300px">Have An Inquiry Or Some Feedback For Us?<br>Fill Out The Form Bellow To Contact Us</p>

  <span class="label" style="left:87px;top:158px">First Name</span>
  <div class="field" style="left:87px;top:180px;width:163px;height:43px">Jane</div>
  <span class="label" style="left:275px;top:158px">Last Name</span>
  <div class="field" style="left:275px;top:180px;width:162px;height:43px">Smith</div>
  <span class="label" style="left:87px;top:244px">Email</span>
  <div class="field" style="left:87px;top:266px;width:350px;height:43px">Jane.Smith@Mailbox.Com</div>
  <span class="label" style="left:87px;top:330px">Message</span>
  <div class="field" style="left:87px;top:352px;width:350px;height:85px"></div>
  <div class="btn btn-solid">Get In Touch</div>

  <div class="map" role="img" aria-label="Dark street map of the city around the office"></div>

  <div class="info" style="left:683px">
    <div class="info-label">Address
      <svg width="9" height="11" viewBox="0 0 9 11"><path d="M4.5 0A4 4 0 0 0 .5 4c0 3 4 7 4 7s4-4 4-7a4 4 0 0 0-4-4z" fill="#0aa89a"/><circle cx="4.5" cy="4" r="1.5" fill="#f4f4f4"/></svg>
    </div>
    <div class="info-value">K. L. Brandts Vej 12, 3.</div>
  </div>
  <div class="divider" style="left:845px"></div>
  <div class="info" style="left:855px">
    <div class="info-label">Our Email
      <svg width="12" height="9" viewBox="0 0 12 9"><rect width="12" height="9" rx="1" fill="#0aa89a"/><path d="M1 1l5 4 5-4" stroke="#f4f4f4" stroke-width="1.2" fill="none"/></svg>
    </div>
    <div class="info-value">K. L. Brandts Vej 12, 3.</div>
  </div>
  <div class="divider" style="left:1018px"></div>
  <div class="info" style="left:1028px">
    <div class="info-label">Phone Number
      <svg width="11" height="11" viewBox="0 0 11 11"><path d="M2 0l2 2.5-1 1.5a7 7 0 0 0 4 4l1.5-1L11 9l-1.5 2C5 11 0 6 0 1.5z" fill="#0aa89a"/></svg>
    </div>
    <div class="info-value">+45 61837420</div>
  </div>
</section>

<footer class="site-footer">
  <div class="footer-brand">Vlm Quarvex</div>
  <nav class="footer-links">
    <span>Home</span><span>Company</span><span>Book Online</span><span>About Us</span><span>FAQs</span><span>Contact US</span>
  </nav>
  <div class="social" aria-label="Social links"><span></span><span></span><span></span><span></span></div>
  <p class="copyright">©2020 By Vlm Quarvex.</p>
</footer>

</body>
</html>
```